Criação de Papelaria Profissional para Beleza
A empresa queria:
" Espaço físico tipo loja com cabines exclusivas para depilação, método Espanhol com cera quente. Única com cauterização pós depilação. E espaço dedicado a beleza das mãos e pés "

```html
<!DOCTYPE html>
<html lang="pt-BR">
<head>
<meta charset="utf-8">
<title>Brisa Cera — Papelaria</title>
<link rel="stylesheet" href="https://fonts.googleapis.com/css2?family=Montserrat:wght@400;500;600&display=swap">
<style>
  :root {
    --backdrop: #ecebe8;
    --plum: #2f2029;
    --pink: #e5208a;
    --pink-soft: #f25aa8;
    --paper: #ffffff;
    --ink-light: #e9dfe6;
    --ghost: #f1f0f1;
  }
  * { box-sizing: border-box; margin: 0; padding: 0; }
  html, body { width: 1200px; height: 1200px; overflow: hidden; }
  body {
    background: var(--backdrop);
    font-family: "Montserrat", sans-serif;
    position: relative;
  }
  .envelope {
    position: absolute;
    width: 470px;
    height: 660px;
    overflow: hidden;
    box-shadow: 0 12px 30px rgba(0,0,0,.12);
  }
  .envelope--dark { left: 90px; top: 270px; background: var(--plum); }
  .envelope--light { left: 640px; top: 270px; background: var(--paper); }

  .envelope__flap { position: absolute; left: 0; top: 0; width: 100%; height: 60px; }
  .envelope__band { position: absolute; left: 0; bottom: 0; width: 100%; height: 60px; }

  .brand {
    position: absolute;
    left: 0; right: 0;
    text-align: center;
    color: var(--pink);
  }
  .envelope--dark .brand { top: 150px; }
  .envelope--light .brand { top: 250px; }
  .brand__name {
    display: inline-flex;
    align-items: center;
    gap: 10px;
    font-weight: 500;
    font-size: 34px;
    letter-spacing: 1px;
  }
  .brand__dot {
    width: 14px; height: 14px;
    border-radius: 50%;
    background: var(--pink);
  }
  .brand__tagline {
    margin-top: 6px;
    font-size: 10px;
    letter-spacing: 3px;
    text-transform: uppercase;
    color: var(--pink);
  }

  .contacts {
    position: absolute;
    left: 28px; right: 28px;
    bottom: 82px;
    display: flex;
    justify-content: space-between;
    color: var(--ink-light);
    font-size: 10px;
    line-height: 1.35;
  }
  .contacts__column { display: flex; flex-direction: column; gap: 10px; }
  .contacts__item { display: flex; align-items: flex-start; gap: 7px; }
  .contacts__icon { width: 14px; height: 14px; flex: none; }
</style>
</head>
<body>

  <section class="envelope envelope--dark" aria-label="Envelope escuro">
    <svg class="envelope__flap" viewBox="0 0 470 60" preserveAspectRatio="none">
      <path d="M0 0 H470 V60 H470 L440 16 H30 L0 60 Z" fill="var(--pink)"/>
    </svg>

    <div class="brand">
      <div class="brand__name"><span class="brand__dot"></span>Brisa Cera</div>
      <div class="brand__tagline">Depilação e Esmaltação</div>
    </div>

    <div class="contacts">
      <div class="contacts__column">
        <div class="contacts__item">
          <svg class="contacts__icon" viewBox="0 0 14 14"><circle cx="7" cy="7" r="7" fill="var(--pink)"/><path d="M4.6 3.6l1.4 1.5-.7 1c.5 1 1.3 1.8 2.3 2.3l1-.7 1.5 1.4-.9 1.3C6.6 10.2 3.8 7.4 3.4 4.5z" fill="var(--plum)"/></svg>
          <span>(00) 0000-0000</span>
        </div>
        <div class="contacts__item">
          <svg class="contacts__icon" viewBox="0 0 14 14"><circle cx="7" cy="7" r="7" fill="var(--pink)"/><rect x="3.5" y="4.5" width="7" height="5" fill="none" stroke="var(--plum)" stroke-width="1"/><path d="M3.5 4.5L7 7.3l3.5-2.8" fill="none" stroke="var(--plum)" stroke-width="1"/></svg>
          <span>contato@brisacera.com</span>
        </div>
      </div>
      <div class="contacts__column">
        <div class="contacts__item">
          <svg class="contacts__icon" viewBox="0 0 14 14"><circle cx="7" cy="7" r="7" fill="var(--pink)"/><circle cx="7" cy="7" r="3.5" fill="none" stroke="var(--plum)" stroke-width="1"/><path d="M3.5 7h7M7 3.5c-1.6 2-1.6 5 0 7M7 3.5c1.6 2 1.6 5 0 7" fill="none" stroke="var(--plum)" stroke-width=".8"/></svg>
          <span>www.brisacera.com.br</span>
        </div>
        <div class="contacts__item">
          <svg class="contacts__icon" viewBox="0 0 14 14"><circle cx="7" cy="7" r="7" fill="var(--pink)"/><path d="M7 11s-3-3-3-5.2a3 3 0 016 0C10 8 7 11 7 11z" fill="var(--plum)"/><circle cx="7" cy="5.8" r="1" fill="var(--pink)"/></svg>
          <span>Rua das Flores, 120 Centro<br>Cidade - UF CEP 00000-000</span>
        </div>
      </div>
    </div>

    <svg class="envelope__band" viewBox="0 0 470 60" preserveAspectRatio="none">
      <path d="M0 14 C 90 14, 150 48, 260 48 H470 V60 H0 Z" fill="var(--pink)"/>
      <path d="M0 6 C 90 6, 150 40, 260 40 H470" fill="none" stroke="var(--pink-soft)" stroke-width="1.5"/>
    </svg>
  </section>

  <section class="envelope envelope--light" aria-label="Envelope claro">
    <div class="brand">
      <div class="brand__name"><span class="brand__dot"></span>Brisa Cera</div>
      <div class="brand__tagline">Depilação e Esmaltação</div>
    </div>

    <svg class="envelope__band" viewBox="0 0 470 60" preserveAspectRatio="none">
      <path d="M0 14 C 90 14, 150 48, 260 48 H470 V60 H0 Z" fill="var(--pink)"/>
      <path d="M0 6 C 90 6, 150 40, 260 40 H470" fill="none" stroke="var(--pink-soft)" stroke-width="1.5"/>
    </svg>
  </section>

</body>
</html>
```